Website Design for Forklift Training Company

DO NOT CONTACT PRIVATELY. ONLY SUBMISSIONS HERE WILL BE CONSIDERED

I need a design for a website that offers forklift training courses.

The company offers accredited, onsite forklift training that are customized for the needs of each individual company. The company offers a variety of courses to operate forklifts and other machinary.

About: "Pembrook Lift Academy Ltd delivers bespoke onsite forklift truck operator training throught the uk.
All our instructors have a wealth of knowledge and expertise to provide your company with all your forklift truck training requirements.
Pembrook Lift Academy Ltd is registered and accredited by qkmvd standards so you can be rest assured that all forklift training is carried out the very highest standard"

I need the following pages designed:
> a) Home Page: Include a header image, ways to contact, about snippet, overview of courses, accreditation that will be received after completing the courses. (See attachments for samples)
> b) About Page
> c) Contact Us Page
> d) Course Page Template: A page that will be used as template for the courses offered. It should contain;
1. Cover image for the course
2. A description of the course
3. A table indicating the various course options
4. Course Objectives
5. What the trainee will receive after doing the course (example: a certification)

Target Market(s)

Industrial Businesses

Number of Pages Required

4 page

Colors
0054AA
0677BA
7BADD7
CADEEF
E8F1F8
0094D4
00A9DD
6FCCEA
C7EBF8
E9F6FB

Requirements
Should not have
• - No Search bar

```html
<!DOCTYPE html>
<html lang="en">
<head>
<meta charset="utf-8">
<title>Contact Page – Website Design</title>
<link rel="stylesheet" href="https://fonts.googleapis.com/css2?family=Roboto:wght@300;400&family=Ubuntu:wght@400;500&display=swap">
<style>
  :root {
    --deep-blue: #0054AA;
    --brand-blue: #0677BA;
    --sky-blue: #0094D4;
    --mist-blue: #E8F1F8;
    --ink: #0B2545;
    --white: #FFFFFF;
    --accent-orange: #F59A48;
    --footer-muted: #9CC7E6;
  }
  * { box-sizing: border-box; margin: 0; padding: 0; }
  html, body { width: 1200px; height: 731px; overflow: hidden; }
  body {
    position: relative;
    font-family: "Ubuntu", sans-serif;
    background: radial-gradient(ellipse 70% 90% at 45% 50%, var(--sky-blue) 0%, var(--brand-blue) 55%, var(--deep-blue) 100%);
  }

  /* Board title */
  .board-title {
    position: absolute; left: 62px; top: 30px;
    font-family: "Roboto", sans-serif; font-weight: 400;
    font-size: 40px; letter-spacing: 0.5px; color: var(--white); line-height: 1;
  }

  .deco-ring { position: absolute; left: 0; top: 0; pointer-events: none; }

  /* Page mockup */
  .page {
    position: absolute; left: 297px; top: 100px; width: 606px; height: 531px;
    background: var(--white); overflow: hidden;
    box-shadow: 0 10px 40px rgba(0, 30, 80, 0.35);
  }
  .nav {
    position: absolute; left: 0; top: 0; width: 100%; height: 42px;
    background: var(--brand-blue);
  }
  .nav a {
    position: absolute; top: 16px; font-size: 7.5px; color: var(--white); text-decoration: none;
  }
  .hero-bg { position: absolute; left: 0; top: 42px; }

  .intro { position: absolute; left: 66px; top: 77px; width: 196px; color: var(--ink); }
  .intro h1 { font-weight: 500; font-size: 20px; line-height: 1; }
  .intro p { margin-top: 9px; font-size: 7.2px; line-height: 12.7px; }

  .contact-item {
    position: absolute; left: 66px; width: 111px; height: 22px;
    display: flex; align-items: center; gap: 7px; padding-left: 7px;
    border: 1px solid var(--brand-blue); background: var(--white);
    font-size: 6.4px; font-weight: 500; color: var(--ink); white-space: nowrap;
  }
  .contact-item svg { width: 9px; height: 9px; fill: currentColor; flex: none; }
  .contact-item--active { background: var(--brand-blue); color: var(--white); }

  .contact-form {
    position: absolute; left: 308px; top: 76px; width: 232px; height: 277px;
    background: var(--brand-blue); border-radius: 3px;
  }
  .contact-form label {
    position: absolute; left: 17px; font-size: 6.5px; font-weight: 500; color: var(--white); line-height: 1;
  }
  .contact-form .field {
    position: absolute; left: 17px; width: 198px; background: var(--white); border-radius: 2px;
  }
  .contact-form .submit {
    position: absolute; left: 124px; top: 237px; width: 91px; height: 22px;
    background: var(--accent-orange); color: var(--white); border-radius: 2px;
    font-size: 8.5px; display: flex; align-items: center; justify-content: center;
  }

  .footer {
    position: absolute; left: 0; top: 430px; width: 100%; height: 101px;
    background: var(--brand-blue); color: var(--white); padding: 19px 0 0 66px;
  }
  .footer h2 { font-weight: 500; font-size: 12.5px; line-height: 1; }
  .footer p { margin-top: 9px; font-size: 6.5px; line-height: 1; color: var(--footer-muted); }
  .footer a { display: block; margin-top: 6px; font-size: 6.5px; line-height: 1; color: var(--footer-muted); }
  .footer__icons { display: flex; gap: 6px; margin-top: 9px; }
  .footer__icons svg { width: 10.5px; height: 10.5px; fill: var(--white); }
</style>
</head>
<body>

  <header class="board-title">CONTACT PAGE</header>

  <svg class="deco-ring" width="1200" height="731" aria-hidden="true">
    <circle cx="1067" cy="584" r="133" fill="none" stroke="#FFFFFF" stroke-width="2.5"/>
  </svg>

  <main class="page">
    <nav class="nav">
      <a href="#" style="left:432px">Home</a>
      <a href="#" style="left:466px">About</a>
      <a href="#" style="left:501px">Courses</a>
      <a href="#" style="left:542px">Contact Us</a>
    </nav>

    <svg class="hero-bg" width="606" height="388" aria-hidden="true">
      <path d="M0 0 H606 V158 Q500 232 303 237 Q106 232 0 158 Z" fill="#E8F1F8"/>
    </svg>

    <section class="intro">
      <h1>Contact Us</h1>
      <p>Qui necessitatibus fuga et odio. Animi aut voluptates dolorem.<br>Blanditiis qui sit voluptatum officia enim.</p>
    </section>

    <div class="contact-item" style="top:189px">
      <svg viewBox="0 0 24 24"><path d="M6.6 10.8a15.1 15.1 0 0 0 6.6 6.6l2.2-2.2a1 1 0 0 1 1-.25 11.4 11.4 0 0 0 3.6.57 1 1 0 0 1 1 1V20a1 1 0 0 1-1 1A17 17 0 0 1 3 4a1 1 0 0 1 1-1h3.5a1 1 0 0 1 1 1c0 1.25.2 2.45.57 3.57a1 1 0 0 1-.25 1z"/></svg>
      +00 1234 5678
    </div>
    <div class="contact-item contact-item--active" style="top:214px">
      <svg viewBox="0 0 24 24"><path d="M20 4H4a2 2 0 0 0-2 2v12a2 2 0 0 0 2 2h16a2 2 0 0 0 2-2V6a2 2 0 0 0-2-2zm0 4-8 5-8-5V6l8 5 8-5z"/></svg>
      info@pembrooklift.example
    </div>
    <div class="contact-item" style="top:240px">
      <svg viewBox="0 0 24 24"><path d="M12 2a7 7 0 0 0-7 7c0 5.250 7 13 7 13s7-7.75 7-13a7 7 0 0 0-7-7zm0 9.5A2.5 2.5 0 1 1 12 6.5a2.5 2.5 0 0 1 0 5z"/></svg>
      48 Quarry Lane 4410
    </div>

    <form class="contact-form">
      <label style="top:15px">Your name</label>
      <div class="field" style="top:27px;height:22px"></div>
      <label style="top:60px">Email</label>
      <div class="field" style="top:72px;height:21px"></div>
      <label style="top:104px">Message</label>
      <div class="field" style="top:116px;height:95px"></div>
      <div class="submit">READ MORE</div>
    </form>

    <footer class="footer">
      <h2>Get In Touch</h2>
      <p>Interested for training with us?</p>
      <a href="#">training@pembrooklift.example</a>
      <div class="footer__icons">
        <svg viewBox="0 0 24 24"><path d="M6.6 10.8a15.1 15.1 0 0 0 6.6 6.6l2.2-2.2a1 1 0 0 1 1-.25 11.4 11.4 0 0 0 3.6.57 1 1 0 0 1 1 1V20a1 1 0 0 1-1 1A17 17 0 0 1 3 4a1 1 0 0 1 1-1h3.5a1 1 0 0 1 1 1c0 1.25.2 2.45.57 3.57a1 1 0 0 1-.25 1z"/></svg>
        <svg viewBox="0 0 24 24"><path d="M20 4H4a2 2 0 0 0-2 2v12a2 2 0 0 0 2 2h16a2 2 0 0 0 2-2V6a2 2 0 0 0-2-2zm0 4-8 5-8-5V6l8 5 8-5z"/></svg>
      </div>
    </footer>
  </main>

</body>
</html>
```